Central Florida Lawn and Landscape business needs an awesome flyer design!

We are a growing lawn and landscape maintenance business looking to incorporate print mail for target advertising. This project should provide some editing capabilities for us to incorporate our logo, update any promotional offers, and adjust throughout the various seasons (lawn service, mulch jobs, one-time clean-ups, hardscape projects, etc). We'd like a clear call to action (one that we can edit if needed) to call or text today. We'll include our website address as well.
The business name is Bolden Yard Crew.
Target Market(s)
Residential homeowners
Industry/Entity Type
Lawn and landscape maintenance
Other font styles liked:
- Couture
Look and feel

```html
<!DOCTYPE html>
<html lang="en">
<head>
<meta charset="UTF-8">
<title>Bolden Yard Crew – Lawn & Landscape Flyer</title>
<link href="https://fonts.googleapis.com/css2?family=Poppins:wght@400;500;600;700;800&family=Oswald:wght@500&display=swap" rel="stylesheet">
<style>
:root{
  --green:#1c9a3e;
  --green-bright:#2fc25a;
  --green-dark:#22502c;
  --ink:#262626;
  --white:#ffffff;
  --text:#2b2b2b;
}
*{margin:0;padding:0;box-sizing:border-box}
html,body{width:949px;height:1200px;overflow:hidden;background:var(--white)}
body{font-family:'Poppins',sans-serif;color:var(--text);position:relative}
.abs{position:absolute}

.brand{left:62px;top:78px;width:332px;text-align:center}
.brand-mark{width:78px;height:78px;border-radius:50%;background:var(--green-dark);margin:0 auto 14px}
.brand-name{font-weight:700;font-size:33px;line-height:1.05;color:var(--green-dark)}

.kicker{left:61px;top:262px;font-size:26px;letter-spacing:8px;font-weight:500;color:var(--ink)}
.headline{left:60px;top:296px;font-size:47px;font-weight:700;line-height:50px;color:var(--green-dark);letter-spacing:-0.5px}
.headline .accent{color:var(--green)}
.experts{left:62px;top:408px;width:292px;height:56px;background:var(--ink);border-radius:5px;color:var(--white);
  font-size:42px;font-weight:500;letter-spacing:15px;text-align:center;line-height:56px;padding-left:10px}
.subline{left:62px;top:481px;font-size:16.5px;line-height:21px;color:var(--ink)}

.hero{left:434px;top:51px}

.why{left:62px;top:562px;width:820px;height:160px}
.why-tab{position:absolute;left:0;top:0}
.why-title{position:absolute;left:34px;top:7px;font-size:19px;font-weight:700;color:var(--white)}
.why-cols{position:absolute;left:0;top:41px;width:820px;height:119px;display:flex;border-bottom-right-radius:26px;overflow:hidden}
.why-col{display:flex;align-items:center;padding-left:18px;gap:16px;color:var(--white);font-size:14px;line-height:17px;font-weight:500}
.why-col.dark{background:var(--green-dark)}
.why-col.light{background:var(--green)}
.why-icon{width:46px;height:46px;border-radius:50%;background:var(--white);border:3px solid var(--green-dark);flex:none}

.section-title{font-size:24px;font-weight:700;color:var(--ink)}
.section-title span{color:var(--green)}
.services-title{left:62px;top:738px}
.service-list{left:62px;top:786px;list-style:none}
.service-list li{display:flex;align-items:center;gap:10px;font-size:14.5px;height:24.5px;line-height:24.5px}
.tick{width:13px;height:13px;flex:none}
.divider{left:352px;top:735px;width:1px;height:275px;background:#dcdcdc}

.seasonal-title{left:378px;top:738px}
.seasonal-box{left:379px;top:761px}
.seasonal-item{display:flex;align-items:flex-start;gap:16px;font-size:14.5px;line-height:17px}
.seasonal-item .tick{margin-top:2px}
.seasonal-left{left:380px}
.seasonal-right{left:640px}

.offer{top:917px;height:90px;border-radius:9px;overflow:hidden;color:var(--white)}
.offer-1{left:375px;width:247px;background:var(--ink)}
.offer-2{left:628px;width:254px;background:var(--green-dark)}
.offer-tab{position:absolute;left:0;top:0}
.offer-label{position:absolute;left:12px;top:4px;font-size:14px;font-weight:500;letter-spacing:0.3px}
.offer-figure{position:absolute;left:11px;top:30px;display:flex;align-items:flex-start;gap:2px}
.offer-num{font-family:'Oswald',sans-serif;font-size:44px;line-height:50px}
.offer-unit{display:flex;flex-direction:column;align-items:center;padding-top:6px}
.offer-pct{font-family:'Oswald',sans-serif;font-size:26px;line-height:26px}
.offer-off{font-size:11px;line-height:13px}
.offer-head{position:absolute;left:96px;top:30px;font-size:11px;font-weight:700;line-height:13px}
.offer-fine{position:absolute;left:96px;font-size:8.5px;line-height:11px}
.offer-ends{position:absolute;left:90px;top:42px;font-size:7.5px;letter-spacing:2px}
.offer-ends b{color:var(--green-bright)}

.thumb{top:1026px;width:137px;height:101px;border:2px solid var(--green-dark);border-radius:3px 14px 3px 14px}
.thumb-1{left:62px;background:linear-gradient(160deg,#4e8a3a,#72b84a 60%,#5aa33c)}
.thumb-2{left:205px;background:linear-gradient(150deg,#3e9a2c,#6cc043 55%,#4ba532)}

.tagline{left:359px;top:1058px;font-size:18px;line-height:22px;color:var(--ink)}
.tagline strong{color:var(--green);font-weight:700}

.contact-title{left:584px;top:1027px;font-size:21px;font-weight:600;color:var(--ink)}
.phone{left:584px;top:1062px;display:flex;align-items:center;gap:14px;font-size:29px;font-weight:700;color:var(--ink)}
.phone-icon{width:28px;height:28px;border-radius:50%;background:var(--green);display:flex;align-items:center;justify-content:center}
.website{left:576px;top:1104px;width:373px;height:27px;background:var(--green-dark);color:var(--white);
  font-size:16px;letter-spacing:4.5px;line-height:27px;padding-left:16px}
</style>
</head>
<body>

<div class="abs brand">
  <div class="brand-mark"></div>
  <div class="brand-name">Bolden Yard Crew</div>
</div>

<div class="abs kicker">YOUR TRUSTED</div>
<div class="abs headline">LOCAL LAWN<br>&amp; <span class="accent">LANDSCAPE</span></div>
<div class="abs experts">EXPERTS</div>
<p class="abs subline">Providing Top-Tier Lawn Care and<br>Landscape Solutions for Every Season</p>

<svg class="abs hero" width="515" height="486" viewBox="0 0 515 486">
  <defs>
    <linearGradient id="lawnPhoto" x1="0" y1="0" x2="0" y2="1">
      <stop offset="0" stop-color="#9a8a70"/>
      <stop offset="0.3" stop-color="#5f8e45"/>
      <stop offset="1" stop-color="#6fbf3a"/>
    </linearGradient>
  </defs>
  <path d="M10 0 H515 V486 H190 Q30 486 14 330 L0 14 Q0 0 10 0 Z" fill="var(--green)"/>
  <rect x="300" y="0" width="215" height="16" fill="var(--green-bright)"/>
  <path d="M31 28 H515 V459 H180 Q62 459 45 320 Z" fill="var(--white)"/>
  <path d="M37 34 H515 V453 H184 Q70 453 52 318 Z" fill="url(#lawnPhoto)" role="img" aria-label="Photo of a man pushing a lawn mower across a green lawn in front of a brick house"/>
</svg>

<section class="abs why">
  <svg class="why-tab" width="820" height="42" viewBox="0 0 820 42">
    <path d="M20 0 H520 Q480 0 460 25 Q447 42 420 42 H0 V20 Q0 0 20 0 Z" fill="var(--ink)"/>
    <path d="M520 0 H820 V42 H420 Q447 42 460 25 Q480 0 520 0 Z" fill="var(--green-dark)"/>
    <path d="M420 42 Q447 42 460 25 Q470 12 485 8 H420 Z" fill="var(--green)"/>
  </svg>
  <h2 class="why-title">Why Choose Bolden Yard Crew?</h2>
  <div class="why-cols">
    <div class="why-col dark" style="width:210px"><span class="why-icon"></span>Reliable<br>Professional<br>Service</div>
    <div class="why-col light" style="width:210px"><span class="why-icon"></span>Custom Lawn<br>&amp; Landscape<br>Plans</div>
    <div class="why-col dark" style="width:196px"><span class="why-icon"></span>Licensed &amp;<br>Insured for<br>Your Peace<br>of Mind</div>
    <div class="why-col light" style="width:204px"><span class="why-icon"></span>Satisfaction<br>Guaranteed</div>
  </div>
</section>

<h2 class="abs section-title services-title">Our <span>Services</span></h2>
<ul class="abs service-list">
  <li><svg class="tick" viewBox="0 0 14 14"><circle cx="7" cy="7" r="7" fill="var(--green-bright)"/><path d="M3.8 7.2 6 9.3 10.3 4.9" stroke="#fff" stroke-width="1.8" fill="none"/></svg>Lawn Care &amp; Maintenance</li>
  <li><svg class="tick" viewBox="0 0 14 14"><circle cx="7" cy="7" r="7" fill="var(--green-bright)"/><path d="M3.8 7.2 6 9.3 10.3 4.9" stroke="#fff" stroke-width="1.8" fill="none"/></svg>Regular Mowing</li>
  <li><svg class="tick" viewBox="0 0 14 14"><circle cx="7" cy="7" r="7" fill="var(--green-bright)"/><path d="M3.8 7.2 6 9.3 10.3 4.9" stroke="#fff" stroke-width="1.8" fill="none"/></svg>Fertilization &amp; Weed Control</li>
  <li><svg class="tick" viewBox="0 0 14 14"><circle cx="7" cy="7" r="7" fill="var(--green-bright)"/><path d="M3.8 7.2 6 9.3 10.3 4.9" stroke="#fff" stroke-width="1.8" fill="none"/></svg>Aeration &amp; Overseeding</li>
  <li><svg class="tick" viewBox="0 0 14 14"><circle cx="7" cy="7" r="7" fill="var(--green-bright)"/><path d="M3.8 7.2 6 9.3 10.3 4.9" stroke="#fff" stroke-width="1.8" fill="none"/></svg>Landscape &amp; Garden Solutions</li>
  <li><svg class="tick" viewBox="0 0 14 14"><circle cx="7" cy="7" r="7" fill="var(--green-bright)"/><path d="M3.8 7.2 6 9.3 10.3 4.9" stroke="#fff" stroke-width="1.8" fill="none"/></svg>Mulching &amp; Bed Maintenance</li>
  <li><svg class="tick" viewBox="0 0 14 14"><circle cx="7" cy="7" r="7" fill="var(--green-bright)"/><path d="M3.8 7.2 6 9.3 10.3 4.9" stroke="#fff" stroke-width="1.8" fill="none"/></svg>Planting &amp; Pruning</li>
  <li><svg class="tick" viewBox="0 0 14 14"><circle cx="7" cy="7" r="7" fill="var(--green-bright)"/><path d="M3.8 7.2 6 9.3 10.3 4.9" stroke="#fff" stroke-width="1.8" fill="none"/></svg>Sod Installation</li>
</ul>
<div class="abs divider"></div>

<h2 class="abs section-title seasonal-title">Seasonal <span>Services</span></h2>
<svg class="abs seasonal-box" width="504" height="140" viewBox="0 0 504 140">
  <path d="M264 1 H478 Q503 1 503 26 V112 Q503 137 478 137 H3" stroke="#8a8a8a" stroke-width="1" fill="none"/>
  <circle cx="3" cy="137" r="2.5" fill="var(--green-dark)"/>
  <line x1="233" y1="30" x2="233" y2="120" stroke="var(--green)" stroke-width="1" stroke-dasharray="3 3"/>
</svg>
<div class="abs seasonal-item seasonal-left" style="top:792px"><svg class="tick" viewBox="0 0 14 14"><circle cx="7" cy="7" r="7" fill="var(--green-dark)"/><path d="M3.8 7.2 6 9.3 10.3 4.9" stroke="#fff" stroke-width="1.8" fill="none"/></svg>Leaf &amp; Debris<br>Clean-up</div>
<div class="abs seasonal-item seasonal-left" style="top:838px"><svg class="tick" viewBox="0 0 14 14"><circle cx="7" cy="7" r="7" fill="var(--green-dark)"/><path d="M3.8 7.2 6 9.3 10.3 4.9" stroke="#fff" stroke-width="1.8" fill="none"/></svg>Snow &amp; Ice Removal</div>
<div class="abs seasonal-item seasonal-left" style="top:865px"><svg class="tick" viewBox="0 0 14 14"><circle cx="7" cy="7" r="7" fill="var(--green-dark)"/><path d="M3.8 7.2 6 9.3 10.3 4.9" stroke="#fff" stroke-width="1.8" fill="none"/></svg>Spring/Fall Clean-ups</div>
<div class="abs seasonal-item seasonal-right" style="top:792px"><svg class="tick" viewBox="0 0 14 14"><circle cx="7" cy="7" r="7" fill="var(--green-dark)"/><path d="M3.8 7.2 6 9.3 10.3 4.9" stroke="#fff" stroke-width="1.8" fill="none"/></svg>Hardscaping Projects</div>
<div class="abs seasonal-item seasonal-right" style="top:823px"><svg class="tick" viewBox="0 0 14 14"><circle cx="7" cy="7" r="7" fill="var(--green-dark)"/><path d="M3.8 7.2 6 9.3 10.3 4.9" stroke="#fff" stroke-width="1.8" fill="none"/></svg>Patios &amp; Walkways</div>
<div class="abs seasonal-item seasonal-right" style="top:853px"><svg class="tick" viewBox="0 0 14 14"><circle cx="7" cy="7" r="7" fill="var(--green-dark)"/><path d="M3.8 7.2 6 9.3 10.3 4.9" stroke="#fff" stroke-width="1.8" fill="none"/></svg>Retaining Walls</div>

<div class="abs offer offer-1">
  <svg class="offer-tab" width="247" height="24" viewBox="0 0 247 24"><path d="M0 0 H148 Q138 0 132 12 Q126 24 112 24 H0 Z" fill="var(--green-dark)"/></svg>
  <div class="offer-label">SPECIAL OFFER</div>
  <div class="offer-figure">
    <span class="offer-num">20</span>
    <span class="offer-unit"><span class="offer-pct">%</span><span class="offer-off">OFF</span></span>
  </div>
  <div class="offer-head">YOUR FIRST LAWN<br>CARE SERVICE!</div>
  <div class="offer-fine" style="top:59px">Call or text today to schedule<br>your <b>FREE CONSULTATION.</b></div>
</div>
<div class="abs offer offer-2">
  <svg class="offer-tab" width="254" height="24" viewBox="0 0 254 24"><path d="M0 0 H150 Q140 0 134 12 Q128 24 114 24 H0 Z" fill="var(--green)"/></svg>
  <div class="offer-label">WINTER SPECIAL</div>
  <div class="offer-figure">
    <span class="offer-num">10</span>
    <span class="offer-unit"><span class="offer-pct">%</span><span class="offer-off">OFF</span></span>
  </div>
  <div class="offer-head" style="left:90px;top:29px;font-size:10.5px">SNOW REMOVAL SERVICES</div>
  <div class="offer-ends">OFFER ENDS <b>TILL 01.01.25</b></div>
  <div class="offer-fine" style="left:90px;top:55px">Fall Clean-Up Special:<br>Free Leaf Removal with Any Lawn<br>Care Package</div>
</div>

<div class="abs thumb thumb-1" role="img" aria-label="Photo of a worker mowing a lawn beside a garden"></div>
<div class="abs thumb thumb-2" role="img" aria-label="Photo of a red lawn mower on freshly cut grass"></div>

<p class="abs tagline">Let’s make your<br>lawn the envy of<br><strong>The Neighborhood!</strong></p>

<div class="abs contact-title">Contact Us Today!</div>
<div class="abs phone">
  <span class="phone-icon"><svg width="15" height="15" viewBox="0 0 24 24"><path d="M6.6 10.8a15.2 15.2 0 0 0 6.6 6.6l2.2-2.2c.3-.3.7-.4 1-.2 1.1.4 2.3.6 3.6.6.6 0 1 .4 1 1V20c0 .6-.4 1-1 1A17 17 0 0 1 3 4c0-.6.4-1 1-1h3.5c.6 0 1 .4 1 1 0 1.3.2 2.5.6 3.6.1.3 0 .7-.2 1z" fill="#fff"/></svg></span>
  867 555 0142
</div>
<div class="abs website">www.boldenyardcrew.com</div>

</body>
</html>
```